Bloom and Rise Website Design (design layout only)

We need a website design for a new nonprofit organization based in Des Moines, Iowa called Bloom and Rise. The nonprofit provides soccer training opportunities to youth soccer players looking to improve their game while also affecting the lives of the less fortunate in a positive way. While participating in the training programs the players also go out and raise money for selected charities. The organization then donates the funds. In its first 18 months we donated $10,500. We would like to see designs attempt to symbolize the mission of the nonprofit - essentially "improve you while improving someone else."

We would like to see the following features:

· A place to donate - Our intent is to have the home page linked to the donation page; a simple straight-forward process for people to give money, and make donating as painless as possible - no account needed to make a donation, credit card or e-check should be the only information needed to donate, and have it be on a single page.

· A photo gallery so people can browse the photo gallery to get a better understanding of our organization and a place to add videos and a calendar to show upcoming events

· A place for contact information and the profiles of directors and board members. This should include a spot showing all the charities the organization donates to. Also includes a news section/blog for comments and suggestions.

We want the design to revolve around the content and mission. We would really like to stress our organization as nonprofit. We would also like if the website was user friendly and easy to navigate.

The logo of our organization is uploaded

```html
<!DOCTYPE html>
<html lang="en">
<head>
<meta charset="utf-8">
<title>Bloom and Rise</title>
<link href="https://fonts.googleapis.com/css2?family=Crimson+Text:wght@400;600&family=PT+Sans:wght@400;700&family=Open+Sans:wght@400;600&display=swap" rel="stylesheet">
<style>
:root{
  --black:#161616;
  --nav-line:#2a2a2a;
  --green:#6cb30e;
  --green-light:#79c21a;
  --green-dark:#3f5c23;
  --green-text:#7a9a4e;
  --date-green:#3d5a1e;
  --grey-text:#9a9a9a;
  --heading:#1c1c1c;
  --rule:#e6e6e6;
  --white:#ffffff;
}
*{margin:0;padding:0;box-sizing:border-box}
html,body{width:913px;height:1200px;overflow:hidden;background:var(--white)}
body{position:relative;font-family:'Open Sans',sans-serif}
.abs{position:absolute}

.topbar{left:0;top:0;width:913px;height:88px;background:var(--black)}
.brand{left:132px;top:22px;display:flex;align-items:center;gap:10px}
.brand-mark{width:36px;height:36px;background:var(--green)}
.brand-name{font-family:'PT Sans',sans-serif;font-weight:700;font-size:22px;color:var(--green-light);line-height:22px;text-transform:uppercase;width:150px}
.nav{left:408px;top:0;height:88px;display:flex}
.nav a{display:flex;align-items:center;justify-content:center;height:88px;color:var(--white);font-size:11px;text-decoration:none;border-right:1px solid var(--nav-line)}
.nav a:first-child{border-left:1px solid var(--nav-line)}
.nav a.active{background:var(--green)}
.social{left:731px;top:41px;display:flex;gap:15px}
.social span{width:8px;height:8px;background:var(--white)}

.donate-band{left:0;top:88px;width:913px;height:137px;background:linear-gradient(#76bd14,#65a90c);border-bottom:2px solid #5a9a0a}
.tagline{left:143px;top:114px;font-family:'PT Sans',sans-serif;font-weight:400;font-size:23px;line-height:27px;letter-spacing:.4px;color:var(--white);text-transform:uppercase}
.willing{left:460px;top:126px;width:94px;text-align:right;font-family:'PT Sans',sans-serif;font-size:14px;line-height:15px;color:var(--white)}
.amount{left:564px;top:119px;width:114px;height:47px;background:var(--green-dark);color:var(--white);font-family:'PT Sans',sans-serif;font-size:16px;display:flex;align-items:center;justify-content:center}
.donate-btn{left:683px;top:119px;width:99px;height:47px;background:var(--black);color:var(--white);font-family:'PT Sans',sans-serif;font-size:16px;display:flex;align-items:center;justify-content:center}

.hero{left:130px;top:187px;width:653px;height:385px;
  background:
    linear-gradient(180deg,rgba(70,110,50,.55) 0%,rgba(0,0,0,0) 18%,rgba(0,0,0,0) 70%,rgba(90,120,70,.5) 100%),
    linear-gradient(90deg,#d8d8d4 0%,#e6e6e2 12%,#2c2c2c 22%,#e2e2de 32%,#3466b8 40%,#2f5da8 50%,#262626 58%,#e06a2a 64%,#1f1f1f 70%,#d9d9d6 80%,#262626 88%,#cfcfcc 100%);
  filter:blur(0)}
.hero-caption{left:130px;top:520px;width:653px;height:52px;background:rgba(20,20,20,.82)}
.hero-caption p{position:absolute;left:12px;top:14px;font-family:'Crimson Text',serif;font-size:16px;color:var(--white)}
.dots{right:18px;top:20px;display:flex;gap:4px}
.dots span{width:11px;height:11px;border-radius:50%;background:#111}
.dots span:first-child{background:var(--white)}

.section-title{font-family:'Crimson Text',serif;font-weight:400;font-size:26px;color:var(--heading);text-transform:uppercase;letter-spacing:.5px}
.arrows{left:280px;top:602px;display:flex;gap:7px}
.arrows svg{width:23px;height:23px}
.gallery-photo{left:139px;top:643px;width:195px;height:173px;border:1px solid #cfd8c4;
  background:
    linear-gradient(90deg,rgba(0,0,0,0) 20%,rgba(200,40,40,.55) 35%,rgba(200,40,40,.5) 48%,rgba(40,80,190,.6) 58%,rgba(40,80,190,.5) 72%,rgba(0,0,0,0) 85%),
    linear-gradient(#f2f4f5 0%,#e6ecee 35%,#7fae4e 48%,#5f9a38 100%)}

.event-thumb{left:380px;width:99px;height:85px;border:1px solid #cfd8c4;border-radius:2px}
.event-thumb.one{top:643px;background:
    linear-gradient(90deg,rgba(0,0,0,0) 15%,rgba(30,160,120,.55) 28%,rgba(0,0,0,0) 42%,rgba(240,200,40,.55) 62%,rgba(0,0,0,0) 80%),
    linear-gradient(#cfe0ec 0%,#9fbfd4 30%,#7ab04c 45%,#69a03e 100%)}
.event-thumb.two{top:733px;background:
    linear-gradient(#3f7fcf 0%,#7fa8da 30%,#8d8a78 42%,#6fa648 58%,#5f9238 100%)}
.event{left:494px;width:292px}
.event-date{display:flex;align-items:center;gap:10px;font-family:'Crimson Text',serif;font-size:16px;color:var(--date-green)}
.event-title{font-family:'Crimson Text',serif;font-size:15px;color:var(--green-text);margin-top:4px}
.event-text{font-size:8.6px;line-height:12px;color:var(--grey-text);margin-top:1px;letter-spacing:-.1px}

.rule{left:130px;top:856px;width:653px;height:1px;background:var(--rule)}

.avatar{left:132px;width:96px;height:96px;border-radius:50%;border:1px solid #cfcfcf}
.avatar.director{background:linear-gradient(#f4f4f4 0%,#e9e9e9 40%,#3a3a3a 80%,#2a2a2a 100%)}
.avatar.member{background:linear-gradient(#f6f6f6 0%,#efe4e0 45%,#3b2a26 75%,#e66a9a 100%)}
.profile{left:242px;width:150px}
.profile h3{font-family:'Crimson Text',serif;font-weight:400;font-size:18px;color:var(--green-text)}
.profile p{font-size:8.5px;line-height:12px;color:var(--grey-text);margin-top:3px}
.profile-btn{display:flex;align-items:center;justify-content:center;width:79px;height:24px;border:1px solid #cfcfcf;font-family:'Crimson Text',serif;font-size:10px;color:var(--grey-text);margin-top:7px}

.video{left:410px;top:927px;width:373px;height:199px;border-radius:4px;border:1px solid #cfcfcf;
  background:
    radial-gradient(ellipse at 55% 55%,rgba(210,170,140,.75) 0%,rgba(0,0,0,0) 55%),
    linear-gradient(135deg,#2d4f8a 0%,#6a5a52 40%,#3f5f2e 100%);overflow:hidden}
.play{left:148px;top:45px}
.video-label{left:0;top:127px;width:373px;text-align:center;font-family:'Crimson Text',serif;font-size:27px;color:var(--white)}

.footer{left:0;top:1155px;width:913px;height:45px;background:var(--black);color:var(--white);font-family:'Crimson Text',serif;font-size:10px;display:flex;align-items:center;justify-content:center}
</style>
</head>
<body>
<header class="topbar abs"></header>
<div class="brand abs"><span class="brand-mark"></span><span class="brand-name">Bloom and Rise</span></div>
<nav class="nav abs">
  <a class="active" href="#" style="width:53px">HOME</a>
  <a href="#" style="width:58px">ABOUT</a>
  <a href="#" style="width:78px">DONATION</a>
  <a href="#" style="width:48px">BLOG</a>
  <a href="#" style="width:70px">CONTACT</a>
</nav>
<div class="social abs"><span></span><span></span></div>

<section class="donate-band abs"></section>
<h1 class="tagline abs">Help them to<br>make their dreams</h1>
<p class="willing abs">I Am Willing<br>to give</p>
<div class="amount abs">$10,500</div>
<div class="donate-btn abs">DONATE</div>

<div class="hero abs" role="img" aria-label="Youth soccer teams and referees lined up on the field"></div>
<div class="hero-caption abs">
  <p>Improve You While Improving Someone Else !</p>
  <div class="dots abs"><span></span><span></span><span></span></div>
</div>

<h2 class="section-title abs" style="left:138px;top:596px">Gallery</h2>
<div class="arrows abs">
  <svg viewBox="0 0 23 23"><circle cx="11.5" cy="11.5" r="11.5" fill="#161616"/><path d="M13 7.5 9 11.5 13 15.5" stroke="#fff" stroke-width="1.6" fill="none"/></svg>
  <svg viewBox="0 0 23 23"><circle cx="11.5" cy="11.5" r="11.5" fill="#161616"/><path d="M10 7.5 14 11.5 10 15.5" stroke="#fff" stroke-width="1.6" fill="none"/></svg>
</div>
<div class="gallery-photo abs" role="img" aria-label="Two young players contesting the ball during a match"></div>

<h2 class="section-title abs" style="left:378px;top:596px">Events</h2>
<div class="event-thumb one abs" role="img" aria-label="Children playing soccer on a grass field"></div>
<div class="event-thumb two abs" role="img" aria-label="Youth match with mountains in the background"></div>

<div class="event abs" style="top:645px">
  <div class="event-date"><svg width="25" height="22" viewBox="0 0 25 22"><rect x="1" y="3" width="23" height="18" rx="2" fill="none" stroke="#3d5a1e" stroke-width="2"/><rect x="1" y="3" width="23" height="5" fill="#3d5a1e"/><g fill="#3d5a1e"><rect x="5" y="10" width="3" height="3"/><rect x="11" y="10" width="3" height="3"/><rect x="17" y="10" width="3" height="3"/><rect x="5" y="15" width="3" height="3"/><rect x="11" y="15" width="3" height="3"/><rect x="17" y="15" width="3" height="3"/></g><rect x="6" y="0" width="2" height="5" fill="#3d5a1e"/><rect x="17" y="0" width="2" height="5" fill="#3d5a1e"/></svg>29 JULY 2014</div>
  <div class="event-title">Lorem ipsum dolor</div>
  <p class="event-text">Lorem ipsum dolor sit amet,consectetuer adipiscing elit,sed .adipiscing elitLorem ipsum dolor sit amet,consectetuer adipiscing elit,sed .adipiscing elit</p>
</div>
<div class="event abs" style="top:737px">
  <div class="event-date"><svg width="25" height="22" viewBox="0 0 25 22"><rect x="1" y="3" width="23" height="18" rx="2" fill="none" stroke="#3d5a1e" stroke-width="2"/><rect x="1" y="3" width="23" height="5" fill="#3d5a1e"/><g fill="#3d5a1e"><rect x="5" y="10" width="3" height="3"/><rect x="11" y="10" width="3" height="3"/><rect x="17" y="10" width="3" height="3"/><rect x="5" y="15" width="3" height="3"/><rect x="11" y="15" width="3" height="3"/><rect x="17" y="15" width="3" height="3"/></g><rect x="6" y="0" width="2" height="5" fill="#3d5a1e"/><rect x="17" y="0" width="2" height="5" fill="#3d5a1e"/></svg>29 JULY 2014</div>
  <div class="event-title">Lorem ipsum dolor</div>
  <p class="event-text">Lorem ipsum dolor sit amet,consectetuer adipiscing elit,sed .adipiscing elitLorem ipsum dolor sit amet,consectetuer adipiscing elit,sed .adipiscing elit</p>
</div>

<div class="rule abs"></div>

<h2 class="section-title abs" style="left:132px;top:875px">Profiles</h2>
<div class="avatar director abs" style="top:923px" role="img" aria-label="Portrait of the director"></div>
<div class="profile abs" style="top:924px">
  <h3>Director</h3>
  <p>Lorem ipsum dolor sit amet, ssgbgh sconsectetuer adipiscing elit,ZDSSsa consectetuer adipiscing elit, sed .</p>
  <div class="profile-btn">PROFILE</div>
</div>
<div class="avatar member abs" style="top:1034px" role="img" aria-label="Portrait of a board member"></div>
<div class="profile abs" style="top:1035px">
  <h3>Member</h3>
  <p>Lorem ipsum dolor sit amet, ssgbgh sconsectetuer adipiscing elit,ZDSSsa consectetuer adipiscing elit, sed .</p>
  <div class="profile-btn">PROFILE</div>
</div>

<h2 class="section-title abs" style="left:411px;top:875px">Video</h2>
<div class="video abs" role="img" aria-label="Team hands joined together over a soccer ball">
  <svg class="play abs" width="78" height="78" viewBox="0 0 78 78"><circle cx="39" cy="39" r="36" fill="rgba(255,255,255,.15)" stroke="rgba(255,255,255,.75)" stroke-width="4"/><path d="M30 22 57 39 30 56Z" fill="rgba(255,255,255,.8)"/></svg>
  <div class="video-label abs">Watch A Video</div>
</div>

<footer class="footer abs">Bloom and Rise © 2014 Privacy Policy</footer>
</body>
</html>
```